Calorie website redesign while keeping current structure

****UPDATE****
Dear designers!

I'd really appreciate to see new color ideas.
The green-red-yellow scheme is the old scheme, and I want to change it. I asked for new colors with same structure, but I get designs with old colors and new structure. :(

My goal is to get a design with a good overall impression.
I need new color ideas where colors are in harmony and gives pleasant OVERALL impression to the eyes.

Your tools again:
1. you can use any colors (i prefer green and blue variations as the most dominant color)
2. you can use gradients
3. you can use transparency.
4. you can use background images.
5. you can change font type (but stay compatible with other languages like Hungarian)

All designs I got so far was not usable because they were not compatible with the site structure.
It was written in description we have fixed sizes, and what you can change and what you CANT change.

Note: i dont like white color. It looks empty and it doesnt give a character to the site.

Separation: it's important the site parts to be easily separated by the eye. The site consists of 4 main parts: menu, what did you eat, what did you do, and yellow calculation boxes. They should be separated easily by looking at it.
*****END OF UPDATE****

DEAR DESIGNERS!

My name is Zsolt, I run this website tornelviqa.hu which is the most popular calorie counting website in Hungary with 500.000 users. It has also an English version, fendrowix.com (started not long ago). Now you have to focus only on the mobile version main page:
https://fendrowix.com/?layout=m

There a lot of other urgent tasks about the site and I had no chance to improve the design in the last years . But I'm aware of the problem: the website doesn't look good enough to be appealing for new users. So now I decided to run a contest to see if you can help me with this.

UNDERSTANDING CURRENT DESIGN CONCEPT:

1. The original concept of the site was that calories are "bad" so they are red color, and sport activites are "good", so they are green color. Red and green is very different color (which is advantage in separating those sections), but they don't look nice together, so I'm ready to change the colors but somehow we still need to show that calories are "bad" and sports are "good". The yellow boxes are showing calculated numbers.
2. The original concept was that I wanted the whole site to have a "calculator feeling": the message is that it is not made to attract people by fancy design, but it's strongness is it's knowledge and usability, same as a hand calculator. I want to maintain this concept, but with a more modern design.
3. Another concept is that I want to make the usability easier for long time users instead of first time users. It means I prefer to show more options/buttons on the screen (which can be frightening to new users, but it's okay), instead of having a very easy-to-use feeling when you first visit our site (but later you need to click a lot to reach functions). Number one priority is still long time usability.
4. I want to emphasise I love to use colors to separate parts.

SUMMARY:

i know it's not easy to make it look better AND compatible current structure, it's a big challenge. Be creative and use your imaginations. It's possible that I will need further adjustments from winning designer in the future, so it's a plus if you will be available to work.

Thanks,
Zsolt Benkő
Updates

I got a car accident, and couldnt leave the countryside. i cant view and review works from here. I will send u an image tomorrow afternoon showing the fixed structure, to avoid misunderstandings in future. so far none of the design is usable, because they were NOT created in our 40px size/5px space structure as i requested in posting thanks for understanding

Received designs were not compatible with structure. It was written in the description, but now I also I updated the description to give a more clear view what I need.

Target Market(s)

weight-loss

Industry/Entity Type

Weight

Number of Pages Required

1 page

Font styles to use
Sans Serif

Colors

Designer to choose colors to be used in the design.

Requirements
Must have
• WHAT CHANGES AM I EXPECTING FROM YOU?
• 1. you can use new colors totally freely along all site.
• 2. You can add some color overlays, gradients, backgrounds, to different sections.
• 3. You can add new edges (delete /increase edges) to buttons/rows (without changing the size).
• 6. If you use new font, then it should be 100% compatible with different languages (for example: Hungarian characters like ö, ő, ü, ű, etc).
• 2. I need better design for input fields (currently inactive is red, and active is white, but you can change it)
• OTHER IMPORTANT NOTES:
• 1. Be careful with technologies which could cause performance issues, as site speed is very important.
• 2. The main goal now is NOT to get new images on buttons (it's perfectly okay if you dont touch them), but an overall better and consistent look. However if you want to achieve this goal by also redesigning buttons and rows (new color, new active/press effect, ), you can do this too. In current version buttons are 40x40, but in new design they will be 80x80.
• 3. The new color concept needs to be compatible with meal colors like breakfast, dinner, etc.
• 4. I love flat design, but I want to encourage you not to limit your imagination. I really appreciate creative ideas, flat or not.
• 5. I want a mobil app athmosphere. Most of the similar sites use so simple designs that they look like settings menu of your phone. I find them very boring, I want to separate sections with nice colors (maybe backgrounds).
• 6. Clear visibility is also important so try to avoid hurting it with too many new design elements.
• 7. First I need only a picture about the new design showing the main page with added meal rows. But of course in the end I need the winning design in a format which I we can use also to sub-menus and desktop version of the site.
Should not have
• WHAT YOU SHOULD NOT CHANGE:
• The menu structure, positions, the buttons sizes. The button animations and sub-menus are all based on this structure, where we use 5px spacing, and 40px rows, and buttons (however we want to double the resolution for these ones: 10 and 80px). We cannot change this basic structure, because it needs a lot of programming, so you need to be creative to make it look better with current structure.

```html
<!DOCTYPE html>
<html lang="en">
<head>
<meta charset="utf-8">
<title>Tornelviqa – Today</title>
<link href="https://fonts.googleapis.com/css2?family=Roboto:wght@400;500;700&display=swap" rel="stylesheet">
<style>
  :root{
    --navy:#0d3156;
    --green-dark:#0f6a2f;
    --green:#21a35f;
    --green-light:#2bb571;
    --input:#e9ecef;
    --placeholder:#8a8f94;
    --white:#ffffff;
    --cell:#f3f7f4;
  }
  *{box-sizing:border-box;margin:0;padding:0}
  html,body{width:1200px;height:3274px;overflow:hidden;background:#cfd6d2}
  body{font-family:"Roboto",Arial,sans-serif;color:var(--white)}
  .stage{position:absolute;left:0;top:0;width:320px;height:873px;transform:scale(3.75);transform-origin:0 0;overflow:hidden}
  .backdrop{position:absolute;inset:0;background:radial-gradient(ellipse at 30% 40%,#a9b5a6 0%,#c7cfc9 45%,#d9dedb 100%)}
  .box{position:absolute;display:flex;align-items:center;justify-content:center}
  .nav{background:var(--navy)}
  .brand{left:5px;top:5px;width:83px;height:40px;font-weight:700;font-size:11px}
  .date-pick{left:95px;top:5px;width:135px;height:40px;gap:6px;font-size:14px}
  .menu{left:237px;top:5px;width:78px;height:40px}
  .prev{left:5px;top:52px;width:40px;height:40px}
  .day{left:50px;top:52px;width:220px;height:40px;font-weight:700;font-size:15px;letter-spacing:.3px}
  .day svg{position:absolute;right:22px}
  .next{left:275px;top:52px;width:40px;height:40px}
  .budget{left:5px;top:98px;width:263px;height:40px;background:var(--green)}
  .budget .fill{position:absolute;left:3px;top:3px;width:125px;height:34px;background:var(--green-dark)}
  .budget .ratio{position:absolute;left:127px;top:3px;font-size:12px;line-height:15px}
  .budget .left-today{position:absolute;right:8px;top:19px;font-size:12px;line-height:15px;white-space:nowrap}
  .gear{left:270px;top:98px;width:45px;height:40px;background:var(--green)}
  .search{left:5px;top:143px;width:263px;height:40px;background:var(--input);justify-content:space-between;padding:0 8px 0 17px;color:var(--placeholder);font-size:16px}
  .search .tools{display:flex;gap:4px;align-items:center}
  .more{width:40px;height:40px;background:var(--green-dark);left:275px}
  .chips{position:absolute;left:5px;width:310px;display:flex;gap:4px}
  .chip{flex:1;height:18px;background:var(--green);font-size:8px;display:flex;align-items:center;padding-left:3px;white-space:nowrap;overflow:hidden}
  .row{position:absolute;left:5px;width:220px;height:40px}
  .food{background:var(--green-dark);font-size:14px;line-height:17px;padding:3px 52px 3px 12px}
  .meal{left:78px;width:147px;background:var(--green-light);font-size:14px;display:flex;align-items:center;padding-left:10px}
  .total{background:var(--green-dark);font-weight:700;font-size:13px;display:flex;align-items:center;padding-left:11px}
  .kcal{position:absolute;right:8px;top:4px;text-align:center;font-size:14px;line-height:15px;font-weight:400}
  .kcal small{display:block;font-size:8px;line-height:10px}
  .macros{position:absolute;left:228px;width:42px;height:40px;display:flex;flex-direction:column;gap:1px;padding-top:1px}
  .macro{height:12px;display:flex;font-size:6.5px;font-weight:700}
  .macro b{width:17px;padding-left:2px;line-height:12px}
  .macro span{flex:1;margin:1px;background:var(--cell);color:#333;text-align:right;padding-right:2px;line-height:10px}
  .p,.f{background:var(--green)}
  .ch{background:var(--navy)}
</style>
</head>
<body>
<div class="stage">
  <div class="backdrop" role="img" aria-label="Soft blurred photo of a plate of fresh food behind the page"></div>

  <div class="box nav brand">Tornelviqa</div>
  <div class="box nav date-pick">a
    <svg width="14" height="16" viewBox="0 0 14 16"><rect x="1" y="2" width="12" height="13" fill="#fff"/><rect x="1" y="2" width="12" height="3" fill="#7fb2e5"/><text x="7" y="13" font-size="8" text-anchor="middle" fill="#0d3156" font-family="Roboto">1</text></svg>
    <svg width="16" height="16"><circle cx="8" cy="8" r="7" fill="#fff"/><text x="8" y="11.5" font-size="9" text-anchor="middle" fill="#0d3156" font-family="Roboto">8</text></svg>
  </div>
  <div class="box nav menu"><svg width="28" height="22"><rect y="1" width="28" height="3.5" rx="1.5" fill="#fff"/><rect y="9" width="28" height="3.5" rx="1.5" fill="#fff"/><rect y="17" width="28" height="3.5" rx="1.5" fill="#fff"/></svg></div>

  <div class="box nav prev"><svg width="12" height="16"><path d="M11 0V16L0 8Z" fill="#fff"/></svg></div>
  <div class="box nav day">TODAY
    <svg width="14" height="17"><rect x="1" y="2" width="12" height="14" fill="none" stroke="#fff" stroke-width="1.3"/><rect x="4" y="0.5" width="6" height="3" fill="#fff"/><path d="M3.5 7h7M3.5 10h7M3.5 13h7" stroke="#fff" stroke-width="1"/></svg>
  </div>
  <div class="box nav next"><svg width="12" height="16"><path d="M1 0V16L12 8Z" fill="#fff"/></svg></div>

  <div class="box budget"><div class="fill"></div><div class="ratio">447/2181</div><div class="left-today">You can eat 1734 more kcal today.</div></div>
  <div class="box gear"><svg width="22" height="22" viewBox="0 0 24 24"><path fill="#fff" d="M19.4 13a7.5 7.5 0 0 0 0-2l2.1-1.6-2-3.5-2.5 1a7.6 7.6 0 0 0-1.700-1L15 3h-4l-.4 2.9a7.6 7.6 0 0 0-1.7 1l-2.5-1-2 3.5L6.6 11a7.5 7.5 0 0 0 0 2l-2.1 1.6 2 3.5 2.5-1a7.6 7.6 0 0 0 1.7 1L11 21h4l.4-2.9a7.6 7.6 0 0 0 1.7-1l2.5 1 2-3.5ZM13 15.5A3.5 3.5 0 1 1 16.5 12 3.5 3.5 0 0 1 13 15.5Z"/></svg></div>

  <div class="box search">What did you eat?
    <span class="tools">
      <svg width="16" height="14"><path d="M3 1l-3 3 3 3M0 4h8" stroke="#444" stroke-width="1.4" fill="none"/><path d="M11 2v11M8 10l3 3 3-3" stroke="#444" stroke-width="1.4" fill="none"/></svg>
      <svg width="16" height="16"><circle cx="6.5" cy="6.5" r="5" stroke="#444" stroke-width="1.8" fill="none"/><path d="M10 10l5 5" stroke="#444" stroke-width="2"/></svg>
    </span>
  </div>
  <div class="box more" style="top:143px"><svg width="22" height="4"><circle cx="3" cy="2" r="2" fill="#fff"/><circle cx="11" cy="2" r="2" fill="#fff"/><circle cx="19" cy="2" r="2" fill="#fff"/></svg></div>

  <div class="chips" style="top:189px"><span class="chip">Breaded chi</span><span class="chip">Melegszend</span><span class="chip">Turos teszta</span><span class="chip">Kristalycuko</span><span class="chip">Korozottes</span></div>
  <div class="chips" style="top:212px"><span class="chip">Bread, white</span><span class="chip">Raw Chicke</span><span class="chip">Csirkeporko</span><span class="chip">Zold etkezes</span><span class="chip">Zoldsegekke</span></div>

  <div class="row food" style="top:236px">1 g Breaded chicken breast<div class="kcal">2<small>kcal</small></div></div>
  <div class="row meal" style="top:281px">Breakfast<div class="kcal">2<small>kcal</small></div></div>
  <div class="row food" style="top:326px">1 g Breaded chicken breast<div class="kcal">2<small>kcal</small></div></div>
  <div class="row meal" style="top:371px">Mid-morning<div class="kcal">2<small>kcal</small></div></div>
  <div class="row food" style="top:416px">9 g Breaded chicken breast<div class="kcal">19<small>kcal</small></div></div>
  <div class="row meal" style="top:461px">Lunch<div class="kcal">19<small>kcal</small></div></div>
  <div class="row food" style="top:506px">100 g Breaded chicken breast<div class="kcal">210<small>kcal</small></div></div>
  <div class="row food" style="top:551px">100 g Breaded chicken breast<div class="kcal">210<small>kcal</small></div></div>
  <div class="row meal" style="top:596px">Mid-afternoon<div class="kcal">420<small>kcal</small></div></div>
  <div class="row food" style="top:641px">1 g Breaded chicken breast<div class="kcal">2<small>kcal</small></div></div>
  <div class="row meal" style="top:686px">Dinner<div class="kcal">2<small>kcal</small></div></div>
  <div class="row food" style="top:731px">1 g Breaded chicken breast<div class="kcal">2<small>kcal</small></div></div>
  <div class="row meal" style="top:776px">Snack<div class="kcal">2<small>kcal</small></div></div>
  <div class="row total" style="top:821px">TOTAL KCAL INTAKE:<div class="kcal">447<small>kcal</small></div></div>

  <div class="macros" style="top:236px"><div class="macro p"><b>P:</b><span>0</span></div><div class="macro ch"><b>CH:</b><span>0</span></div><div class="macro f"><b>F:</b><span>0</span></div></div>
  <div class="macros" style="top:281px"><div class="macro p"><b>P:</b><span>0</span></div><div class="macro ch"><b>CH:</b><span>0</span></div><div class="macro f"><b>F:</b><span>0</span></div></div>
  <div class="macros" style="top:326px"><div class="macro p"><b>P:</b><span>0</span></div><div class="macro ch"><b>CH:</b><span>0</span></div><div class="macro f"><b>F:</b><span>0</span></div></div>
  <div class="macros" style="top:371px"><div class="macro p"><b>P:</b><span>0</span></div><div class="macro ch"><b>CH:</b><span>0</span></div><div class="macro f"><b>F:</b><span>0</span></div></div>
  <div class="macros" style="top:416px"><div class="macro p"><b>P:</b><span>0</span></div><div class="macro ch"><b>CH:</b><span>0</span></div><div class="macro f"><b>F:</b><span>0</span></div></div>
  <div class="macros" style="top:461px"><div class="macro p"><b>P:</b><span>0</span></div><div class="macro ch"><b>CH:</b><span>0</span></div><div class="macro f"><b>F:</b><span>0</span></div></div>
  <div class="macros" style="top:506px"><div class="macro p"><b>P:</b><span>0</span></div><div class="macro ch"><b>CH:</b><span>0</span></div><div class="macro f"><b>F:</b><span>0</span></div></div>
  <div class="macros" style="top:551px"><div class="macro p"><b>P:</b><span>0</span></div><div class="macro ch"><b>CH:</b><span>0</span></div><div class="macro f"><b>F:</b><span>0</span></div></div>
  <div class="macros" style="top:596px"><div class="macro p"><b>P:</b><span>0</span></div><div class="macro ch"><b>CH:</b><span>0</span></div><div class="macro f"><b>F:</b><span>0</span></div></div>
  <div class="macros" style="top:641px"><div class="macro p"><b>P:</b><span>0</span></div><div class="macro ch"><b>CH:</b><span>0</span></div><div class="macro f"><b>F:</b><span>0</span></div></div>
  <div class="macros" style="top:686px"><div class="macro p"><b>P:</b><span>0</span></div><div class="macro ch"><b>CH:</b><span>0</span></div><div class="macro f"><b>F:</b><span>0</span></div></div>
  <div class="macros" style="top:731px"><div class="macro p"><b>P:</b><span>0</span></div><div class="macro ch"><b>CH:</b><span>0</span></div><div class="macro f"><b>F:</b><span>0</span></div></div>
  <div class="macros" style="top:776px"><div class="macro p"><b>P:</b><span>0</span></div><div class="macro ch"><b>CH:</b><span>0</span></div><div class="macro f"><b>F:</b><span>0</span></div></div>
  <div class="macros" style="top:821px"><div class="macro p"><b>P:</b><span>0</span></div><div class="macro ch"><b>CH:</b><span>0</span></div><div class="macro f"><b>F:</b><span>0</span></div></div>

  <div class="box more" style="top:236px"><svg width="22" height="4"><circle cx="3" cy="2" r="2" fill="#fff"/><circle cx="11" cy="2" r="2" fill="#fff"/><circle cx="19" cy="2" r="2" fill="#fff"/></svg></div>
  <div class="box more" style="top:281px"><svg width="22" height="4"><circle cx="3" cy="2" r="2" fill="#fff"/><circle cx="11" cy="2" r="2" fill="#fff"/><circle cx="19" cy="2" r="2" fill="#fff"/></svg></div>
  <div class="box more" style="top:326px"><svg width="22" height="4"><circle cx="3" cy="2" r="2" fill="#fff"/><circle cx="11" cy="2" r="2" fill="#fff"/><circle cx="19" cy="2" r="2" fill="#fff"/></svg></div>
  <div class="box more" style="top:371px"><svg width="22" height="4"><circle cx="3" cy="2" r="2" fill="#fff"/><circle cx="11" cy="2" r="2" fill="#fff"/><circle cx="19" cy="2" r="2" fill="#fff"/></svg></div>
  <div class="box more" style="top:416px"><svg width="22" height="4"><circle cx="3" cy="2" r="2" fill="#fff"/><circle cx="11" cy="2" r="2" fill="#fff"/><circle cx="19" cy="2" r="2" fill="#fff"/></svg></div>
  <div class="box more" style="top:461px"><svg width="22" height="4"><circle cx="3" cy="2" r="2" fill="#fff"/><circle cx="11" cy="2" r="2" fill="#fff"/><circle cx="19" cy="2" r="2" fill="#fff"/></svg></div>
  <div class="box more" style="top:506px"><svg width="22" height="4"><circle cx="3" cy="2" r="2" fill="#fff"/><circle cx="11" cy="2" r="2" fill="#fff"/><circle cx="19" cy="2" r="2" fill="#fff"/></svg></div>
  <div class="box more" style="top:551px"><svg width="22" height="4"><circle cx="3" cy="2" r="2" fill="#fff"/><circle cx="11" cy="2" r="2" fill="#fff"/><circle cx="19" cy="2" r="2" fill="#fff"/></svg></div>
  <div class="box more" style="top:596px"><svg width="22" height="4"><circle cx="3" cy="2" r="2" fill="#fff"/><circle cx="11" cy="2" r="2" fill="#fff"/><circle cx="19" cy="2" r="2" fill="#fff"/></svg></div>
  <div class="box more" style="top:641px"><svg width="22" height="4"><circle cx="3" cy="2" r="2" fill="#fff"/><circle cx="11" cy="2" r="2" fill="#fff"/><circle cx="19" cy="2" r="2" fill="#fff"/></svg></div>
  <div class="box more" style="top:686px"><svg width="22" height="4"><circle cx="3" cy="2" r="2" fill="#fff"/><circle cx="11" cy="2" r="2" fill="#fff"/><circle cx="19" cy="2" r="2" fill="#fff"/></svg></div>
  <div class="box more" style="top:731px"><svg width="22" height="4"><circle cx="3" cy="2" r="2" fill="#fff"/><circle cx="11" cy="2" r="2" fill="#fff"/><circle cx="19" cy="2" r="2" fill="#fff"/></svg></div>
  <div class="box more" style="top:776px"><svg width="22" height="4"><circle cx="3" cy="2" r="2" fill="#fff"/><circle cx="11" cy="2" r="2" fill="#fff"/><circle cx="19" cy="2" r="2" fill="#fff"/></svg></div>
  <div class="box more" style="top:821px"><svg width="22" height="4"><circle cx="3" cy="2" r="2" fill="#fff"/><circle cx="11" cy="2" r="2" fill="#fff"/><circle cx="19" cy="2" r="2" fill="#fff"/></svg></div>
</div>
</body>
</html>
```